KQR announces Absolutely No Fees!!

TRVO Swift Lending is financial institution operating in the Caribbean . The company is planning to remove all fees from its loan process . The company will charge its customer absolutely no fees. No application fees, no underwriting fees, no origination fees, no late payment fees, no penalty fees, no credit bureau fees, no transaction fees etc etc etc…absolutely no fees.

The company would like to create an advertising campaign that blows the market away with this information. As no other bank/financial institution has this offer.

Target Market(s)

Mass Market - Caribbean

Industry/Entity Type

Banking / Finance

Requirements
Must have
• Please be creative.

```html
<!DOCTYPE html>
<html lang="en">
<head>
<meta charset="utf-8">
<title>TRVO Swift Lending – No Fees</title>
<link href="https://fonts.googleapis.com/css2?family=Bebas+Neue&family=Lato:wght@700;900&display=swap" rel="stylesheet">
<style>
  :root {
    --page-bg: #e8e8e8;
    --card-bg: #ffffff;
    --brand-red: #e5342a;
    --brand-green: #1f8a4b;
    --note-light: #dfe3e2;
    --note-mid: #a9b1b3;
    --note-green: #9cb9a4;
    --note-orange: #d9a273;
  }
  * { margin: 0; padding: 0; box-sizing: border-box; }
  html, body {
    width: 1200px;
    height: 905px;
    overflow: hidden;
    background: var(--page-bg);
  }
  .ad-card {
    position: absolute;
    left: 101px;
    top: 124px;
    width: 996px;
    height: 610px;
    background: var(--card-bg);
    font-family: "Lato", sans-serif;
  }
  .money-photo {
    position: absolute;
    left: 0;
    top: 0;
    width: 409px;
    height: 610px;
    background:
      radial-gradient(circle at 30% 25%, rgba(217,162,115,0.45), transparent 35%),
      radial-gradient(circle at 75% 70%, rgba(156,185,164,0.5), transparent 40%),
      radial-gradient(circle at 20% 85%, rgba(217,162,115,0.4), transparent 35%),
      linear-gradient(160deg, var(--note-light) 0%, var(--note-mid) 45%, var(--note-light) 70%, var(--note-mid) 100%);
  }
  .accent-bar {
    position: absolute;
    right: 0;
    top: 0;
    width: 22px;
    height: 610px;
    background: var(--brand-green);
  }
  .headline {
    position: absolute;
    left: 465px;
    top: 138px;
    font-size: 28.5px;
    font-weight: 700;
    color: var(--brand-red);
    white-space: nowrap;
  }
  .big-no {
    position: absolute;
    left: 462px;
    top: 178px;
    font-family: "Bebas Neue", sans-serif;
    font-size: 318px;
    line-height: 1;
    letter-spacing: 6px;
    color: var(--brand-red);
  }
  .fees-title {
    position: absolute;
    left: 729px;
    top: 188px;
    font-size: 98px;
    font-weight: 900;
    line-height: 1;
    letter-spacing: -2px;
    color: var(--brand-green);
  }
  .fee-list {
    position: absolute;
    left: 734px;
    top: 293px;
    list-style: none;
    font-size: 15.5px;
    font-weight: 900;
    line-height: 19px;
    letter-spacing: 1.6px;
    color: var(--brand-green);
    white-space: nowrap;
  }
  .fee-list .no { color: var(--brand-red); }
  .fee-list .closing { color: var(--brand-red); }
  .brand-name {
    position: absolute;
    left: 566px;
    top: 511px;
    display: flex;
    align-items: center;
    gap: 10px;
    font-size: 28px;
    font-weight: 900;
    color: var(--brand-green);
    white-space: nowrap;
  }
  .brand-mark {
    width: 22px;
    height: 22px;
    background: var(--brand-red);
  }
</style>
</head>
<body>
  <div class="ad-card">
    <div class="money-photo" role="img" aria-label="Scattered hundred-dollar banknotes"></div>

    <p class="headline">Removing all fees from loan process</p>

    <div class="big-no">NO</div>
    <div class="fees-title">Fees</div>

    <ul class="fee-list">
      <li><span class="no">NO</span> application fees</li>
      <li><span class="no">NO</span> underwriting fees</li>
      <li><span class="no">NO</span> origination fees,</li>
      <li><span class="no">NO</span> late payment fees</li>
      <li><span class="no">NO</span> penalty fees</li>
      <li><span class="no">NO</span> credit bureau fees</li>
      <li class="closing">……absolutely no fees</li>
    </ul>

    <div class="brand-name"><span class="brand-mark"></span>TRVO Swift Lending</div>

    <div class="accent-bar"></div>
  </div>
</body>
</html>
```